Verimoss Health - Ashwagandha Bottle Label

Verimoss Health is a supplement brand of ayurvedic supplements and green organic non GMO products. Currently we make tablet supplements but we will be expanding to other products in 2017.

We need a bottle label for an herbal, organic, non-GMO supplement called ashwagandha. The bottle color is amber and the lid is white. We want a bottle lable that will stand out from my competitors that conveys good health. We like the idea of a clean and uncluttered label that is unique and compelling.

Logo and template attached. Let me know if you need a different logo file format.

Some brand labels we like are: Brisk Larder, ourLoft, and voru.

Here are some benefits of Ashwagandha (supported by science) to help you get familiar with what it does. This does not need to be on the label because there isn't much room.
Protects the immune system
Helps combat the effects of stress
Improves learning, memory, and reaction time
Reduces anxiety and depression without causing drowsiness
Helps reduce brain-cell degeneration
Stabilizes blood sugar
Helps lower cholesterol
Offers anti-inflammatory benefits
Contains anti-malarial properties
Enhances sexual potency for both men and women

Images of ashwagandha plant attached in case you want to see what it is.

Logo colors:
Darker green : Pantone 5757C
Lighter green: Pantone 5845C

Target Market(s)

Health and wellmess

Industry/Entity Type

Supplement

Font styles to use
Serif
Sans Serif

Requirements
Must have
• - Rich colors
• - See attached template for label size (it must be the size on template. Thank you.)
Nice to have
• I am open to ideas and your expertise.
Should not have
• - No pastel colors
• - No script fonts
• - No decorative fonts

```html
<!DOCTYPE html>
<html lang="en">
<head>
<meta charset="utf-8">
<title>Verimoss Health – Ashwagandha Label</title>
<link rel="stylesheet" href="https://fonts.googleapis.com/css2?family=PT+Sans:wght@400;700&family=PT+Sans+Narrow:wght@400;700&family=Open+Sans:wght@400;700;800&family=Lato:wght@400&display=swap">
<style>
  :root {
    --bg: #eceeec;
    --label-top: #fbfbf8;
    --label-mid: #e6ebd3;
    --label-bottom: #a9bd5e;
    --brand-green: #7d9a2c;
    --brand-olive: #9c9a58;
    --title-red: #d4263a;
    --ink: #1e1e1e;
    --ink-soft: #3c3c3c;
    --leaf-dark: #3f7d2a;
    --berry: #c8202a;
    --bloom: #e6df8c;
    --tag-green: #6f8c24;
  }
  * { box-sizing: border-box; margin: 0; padding: 0; }
  html, body { width: 1200px; height: 1200px; overflow: hidden; }
  body {
    background: var(--bg);
    font-family: "PT Sans", sans-serif;
    color: var(--ink);
    display: flex;
    align-items: center;
    justify-content: center;
  }
  .label {
    width: 1120px;
    height: 560px;
    display: flex;
    background: linear-gradient(180deg, var(--label-top) 0%, var(--label-top) 30%, var(--label-mid) 62%, var(--label-bottom) 100%);
    box-shadow: 0 6px 24px rgba(0,0,0,.12);
  }
  .panel { position: relative; height: 100%; }

  /* Front */
  .panel--front { width: 540px; text-align: center; padding-top: 58px; }
  .brand {
    font-family: "Lato", sans-serif;
    font-size: 34px;
    letter-spacing: 2px;
    color: var(--brand-olive);
    display: inline-flex;
    align-items: center;
    gap: 10px;
  }
  .brand__dot { width: 12px; height: 12px; border-radius: 50%; background: var(--brand-green); }
  .product-name {
    font-family: "PT Sans", sans-serif;
    font-weight: 400;
    font-size: 78px;
    color: var(--title-red);
    margin-top: 26px;
    letter-spacing: -1px;
    line-height: 1;
  }
  .product-type {
    font-family: "Lato", sans-serif;
    font-size: 22px;
    letter-spacing: 5px;
    color: var(--ink-soft);
    margin-top: 12px;
  }
  .badge-seal {
    position: absolute; left: 34px; top: 250px;
    width: 70px; height: 70px; border-radius: 50%;
    background: #fff; border: 4px solid var(--brand-green);
  }
  .plant-art {
    position: absolute; left: 120px; top: 240px;
    width: 300px; height: 210px;
    border-radius: 40% 50% 45% 40%;
    background: radial-gradient(circle at 40% 55%, var(--berry) 0 14%, var(--bloom) 24%, var(--leaf-dark) 46%, rgba(63,125,42,0) 72%);
  }
  .count-tag {
    position: absolute; right: 40px; top: 360px;
    width: 56px; padding: 4px 0 12px;
    background: var(--tag-green); color: #fff;
    font-family: "PT Sans Narrow", sans-serif; font-weight: 700;
    line-height: 1; text-align: center;
    clip-path: polygon(0 0,100% 0,100% 100%,50% 88%,0 100%);
  }
  .count-tag__top { background: #fff; color: var(--ink); margin: 0 3px 4px; padding: 2px 0; }
  .count-tag__num { font-size: 22px; display: block; }
  .count-tag__unit { font-size: 12px; font-weight: 400; display: block; }
  .tagline {
    position: absolute; left: 0; right: 0; bottom: 30px;
    font-family: "PT Sans Narrow", sans-serif; font-size: 21px;
    color: #5f6d1c;
  }

  /* Back */
  .panel--back { width: 580px; padding: 50px 46px 0 40px; font-family: "PT Sans Narrow", sans-serif; }
  .facts { border: 3px solid var(--ink); padding: 4px 10px 2px; }
  .facts__title { font-family: "Open Sans", sans-serif; font-weight: 800; font-size: 30px; line-height: 1.05; }
  .facts__line { font-family: "Open Sans", sans-serif; font-size: 21px; line-height: 1.1; }
  .facts__rule-heavy { border-top: 6px solid var(--ink); margin: 4px -10px 0; height: 24px; }
  .facts__head { border-top: 3px solid var(--ink); margin: 0 -10px; padding: 2px 10px 0; text-align: right; font-size: 10px; font-weight: 700; line-height: 1.1; }
  .facts__row { display: flex; justify-content: space-between; font-size: 21px; padding: 2px 0; border-top: 1px solid var(--ink); }
  .facts__note { border-top: 3px solid var(--ink); margin: 0 -10px; padding: 2px 10px; font-size: 21px; }
  .ingredients { font-size: 21px; margin-top: 8px; line-height: 1.2; }
  .usage { font-size: 21px; color: var(--brand-green); margin-top: 4px; line-height: 1.2; }
  .usage strong { font-weight: 700; }
  .warning { border: 3px solid var(--ink); padding: 6px 12px; margin-top: 10px; font-size: 20px; line-height: 1.2; text-align: justify; }
  .batch { display: flex; justify-content: space-between; font-size: 21px; margin-top: 16px; }
</style>
</head>
<body>
  <div class="label">
    <section class="panel panel--front">
      <div class="brand"><span>Verimoss Health</span><span class="brand__dot"></span></div>
      <h1 class="product-name">Ashwagandha</h1>
      <p class="product-type">HERBAL SUPPLEMENT</p>
      <div class="badge-seal" role="img" aria-label="Non-GMO seal"></div>
      <div class="plant-art" role="img" aria-label="Illustration of an ashwagandha sprig with red berries, pale husks and green leaves"></div>
      <div class="count-tag">
        <div class="count-tag__top"><span class="count-tag__num">60</span><span class="count-tag__unit">tablets</span></div>
        <span class="count-tag__num">30</span><span class="count-tag__unit">days using</span>
      </div>
      <p class="tagline">Ayurvedic Supplements and Green Organic NON GMO Products</p>
    </section>

    <section class="panel panel--back">
      <div class="facts">
        <div class="facts__title">Supplement Fact</div>
        <div class="facts__line">Serving Size 1 tablet</div>
        <div class="facts__line">Serving per container 60</div>
        <div class="facts__rule-heavy"></div>
        <div class="facts__head">Amount Per<br>Serving</div>
        <div class="facts__row"><span>Organic Ashwagandha (root)</span><span>475mg</span></div>
        <div class="facts__note">† Daily Value not established</div>
      </div>
      <p class="ingredients">Other ingredients, from natural sources:<br>Organic Tapioca starch.</p>
      <p class="usage"><strong>Suggested Use:</strong> 1-2 tablets twice daily, with water after meals.</p>
      <p class="warning"><strong>Important:</strong> if you are pregnant or nursing or have a known medical condition consult your physician before taking this or any other dietary supplement. Store in a cool and dry place, lid tightly. Keep out of reach of children.</p>
      <div class="batch"><span>Batch No:</span><span>Best before:</span></div>
    </section>
  </div>
</body>
</html>
```